Bargain Haven marketing postcard

We are a nonprofit that runs a thrift store to fund our mission. Our mission is to create jobs and independence for people with long term serious mental illnesses. We recently purchased a cargo van for neighborhood pickups and we want to publicize our services. We accept donations of furniture, clothing, electronics, art, and other household items. We are a 501(c)(3) and all donations are potentially tax deductible. We have a logo that is attached below. The phone to call for pickup: (301) 738-7723Our websites: www.brightpathworksinc.org, www.maplecornerthriftshop.org

Target Market(s)

Potential donors

Industry/Entity Type

Marketing

Font styles to use
Serif
Sans Serif

Requirements
Must have
• We are rebranding so I would like to have the new name of the store: Bargain Haven. Also reference to the old name (formerly Maple Corner Thrift Shop). I'd like it to say that it is "a project of Brightpath Works, Inc." and that we are a 501(c)(3). Finally, please mention that we do in-home donation pick-up and provide the contact number.

```html
<!DOCTYPE html>
<html lang="en">
<head>
<meta charset="utf-8">
<title>Bargain Haven postcard</title>
<link href="https://fonts.googleapis.com/css2?family=Arimo:wght@700&family=Didact+Gothic&family=Questrial&display=swap" rel="stylesheet">
<style>
  :root {
    --bg-main: #dfe2e0;
    --bg-top: #d3d3d3;
    --bg-panel: #eef1ef;
    --bg-strip: #c9c9c9;
    --ink: #1f1b1c;
    --ink-soft: #2b2b2b;
    --leaf: #8a9a36;
    --square-dark: #c4c6c5;
    --square-light: #f1f3f2;
  }
  * { margin: 0; padding: 0; box-sizing: border-box; }
  html, body { width: 1200px; height: 774px; overflow: hidden; background: var(--bg-main); }
  .postcard {
    position: relative;
    width: 1200px;
    height: 774px;
    background: var(--bg-main);
    font-family: "Questrial", "Didact Gothic", sans-serif;
    color: var(--ink);
    overflow: hidden;
  }
  .backdrop { position: absolute; inset: 0; }
  .tagline {
    position: absolute;
    top: 40px; left: 0; width: 100%;
    text-align: center;
    font-family: "Didact Gothic", sans-serif;
    font-size: 46px;
    line-height: 1;
    color: var(--ink-soft);
  }
  .brand-mark {
    position: absolute;
    left: 528px; top: 170px;
    width: 144px; height: 144px;
    border-radius: 50%;
    background: var(--leaf);
  }
  .brand-name {
    position: absolute;
    top: 334px; left: 0; width: 100%;
    text-align: center;
    font-family: "Questrial", sans-serif;
    font-weight: 400;
    font-size: 62px;
    line-height: 1;
    color: var(--ink);
  }
  .brand-former {
    position: absolute;
    top: 402px; left: 0; width: 100%;
    text-align: center;
    font-size: 17px;
    line-height: 1;
    color: var(--ink-soft);
  }
  .mission {
    position: absolute;
    top: 433px; left: 0; width: 100%;
    text-align: center;
    font-size: 22px;
    line-height: 30px;
    color: var(--ink);
  }
  .photo-strip { position: absolute; left: 216px; top: 500px; }
  .pickup {
    position: absolute;
    top: 672px; left: 0; width: 100%;
    text-align: center;
    font-size: 21px;
    line-height: 1;
  }
  .websites {
    position: absolute;
    top: 716px; left: 222px;
    font-size: 20.5px;
    line-height: 1;
  }
  .contact-value { font-family: "Arimo", sans-serif; font-weight: 700; }
</style>
</head>
<body>
<main class="postcard">
  <svg class="backdrop" width="1200" height="774" viewBox="0 0 1200 774" aria-hidden="true">
    <path d="M0 0 H1200 V104 Q600 95 0 126 Z" fill="var(--bg-top)"/>
    <rect x="825" y="462" width="375" height="312" fill="var(--bg-panel)"/>
    <rect x="383" y="703" width="817" height="71" fill="var(--bg-strip)"/>
    <rect x="284" y="360" width="23" height="22" fill="var(--square-dark)"/>
    <rect x="300" y="346" width="32" height="32" fill="var(--square-light)"/>
    <rect x="870" y="345" width="25" height="23" fill="var(--square-dark)"/>
    <rect x="885" y="358" width="32" height="32" fill="var(--square-light)"/>
  </svg>

  <p class="tagline">'a project of Brightpath Works, Inc., a 501(c)(3)'</p>

  <div class="brand-mark" aria-hidden="true"></div>
  <h1 class="brand-name">BARGAIN HAVEN</h1>
  <p class="brand-former">formerly Maple Corner Thrift Shop</p>

  <p class="mission">Our mission is to create jobs and independence<br>for people with long term serious mental illnesses</p>

  <svg class="photo-strip" width="778" height="158" viewBox="0 0 778 158" role="img" aria-label="Curved strip of store photos: a staff member among clothing racks, a fireplace mantel and side table, a round wooden table, a white stove, and a staff member at the counter">
    <defs>
      <linearGradient id="stripTone" x1="0" x2="1" y1="0" y2="0">
        <stop offset="0" stop-color="#6f7378"/>
        <stop offset="0.25" stop-color="#8a7660"/>
        <stop offset="0.5" stop-color="#6b5a47"/>
        <stop offset="0.75" stop-color="#9a8e80"/>
        <stop offset="1" stop-color="#8c8f92"/>
      </linearGradient>
    </defs>
    <path d="M2 12 Q389 -6 776 12 V140 Q389 162 2 150 Z" fill="url(#stripTone)" stroke="#444" stroke-width="1.5"/>
  </svg>

  <p class="pickup">Free in-home donation pickup, call: <span class="contact-value">(555) 214-9086</span></p>
  <p class="websites">Our websites: <span class="contact-value">www.brightpathworksinc.org, www.maplecornerthriftshop.org</span></p>
</main>
</body>
</html>
```